Rehab/fitness Business card design

I need a design that promotes "A peak ridge base for movers". services include assessment, massage, physiotherapy, pilates, suspension training, kinesiotaping in any combination.
I would like to bring the design into my website, flyers etc

Target Market(s)

athletes from beginner to elite - any age, male and female

Industry/Entity Type

Shop

Contact Information for Business Card

Peak-Ridge-Base for Movers
17 Halden Rise, Larchmont, Wescombe
027 418 7093
kerry.dunlow@vestmail.test

Logo Text

Logo styles of interest
Abstract Logo
Requirements
Nice to have
• Blue colour theme

```html
<!DOCTYPE html>
<html lang="en">
<head>
<meta charset="utf-8">
<title>Peak-Ridge-Base for Movers – Business Card</title>
<link rel="stylesheet" href="https://fonts.googleapis.com/css2?family=Exo+2:wght@600;700&display=swap">
<style>
  :root {
    --bg: #2b2b2b;
    --blue-light: #1a95d2;
    --blue-mid: #0f78b0;
    --blue-dark: #065a88;
    --white: #ffffff;
    --panel: #ececec;
    --ink: #333a40;
    --accent-blue: #0d7fbf;
    --divider: #6fc3ec;
  }
  * { box-sizing: border-box; margin: 0; padding: 0; }
  html, body { width: 1200px; height: 900px; overflow: hidden; }
  body {
    background: var(--bg);
    font-family: "Exo 2", "Arial", sans-serif;
    position: relative;
  }
  .card {
    position: absolute;
    top: 300px;
    width: 520px;
    height: 300px;
    border-radius: 2px;
    overflow: hidden;
    box-shadow: 0 14px 30px rgba(0,0,0,0.45);
  }
  .card--front {
    left: 50px;
    background: radial-gradient(ellipse at 50% 45%, var(--blue-light) 0%, var(--blue-mid) 55%, var(--blue-dark) 100%);
    display: flex; align-items: center; justify-content: center;
  }
  .brand {
    display: flex; align-items: center;
    color: var(--white);
    font-weight: 700;
    text-transform: uppercase;
    white-space: nowrap;
  }
  .brand-mark { display: block; background: var(--white); }
  .card--front .brand { font-size: 34px; letter-spacing: 1px; gap: 14px; }
  .card--front .brand-mark { width: 26px; height: 26px; }

  .card--back {
    left: 630px;
    background: var(--panel);
  }
  .back-top {
    height: 160px;
    background: radial-gradient(ellipse at 45% 60%, var(--blue-light) 0%, var(--blue-mid) 55%, var(--blue-dark) 100%);
    display: flex; align-items: center; justify-content: space-between;
    padding: 0 24px;
  }
  .back-top .brand { font-size: 13px; letter-spacing: 0.6px; gap: 7px; }
  .back-top .brand-mark { width: 11px; height: 11px; }
  .services {
    list-style: none;
    color: var(--white);
    font-weight: 600;
    font-size: 12px;
    letter-spacing: 1.1px;
    text-transform: uppercase;
    line-height: 1.5;
    display: flex; flex-wrap: wrap;
    width: 310px;
  }
  .services li { white-space: nowrap; }
  .services li + li::before { content: "|"; color: var(--divider); margin: 0 5px; }
  .services li.line-start::before { content: none; }
  .services .break { flex-basis: 100%; height: 0; }
  .back-bottom { padding: 16px 26px 0; }
  .tagline {
    color: var(--accent-blue);
    font-weight: 700;
    font-size: 21px;
    letter-spacing: 1.2px;
    text-transform: uppercase;
  }
  .details {
    display: flex; justify-content: space-between;
    margin-top: 10px;
    color: var(--ink);
    font-weight: 600;
  }
  .address { font-size: 11px; letter-spacing: 0.8px; text-transform: uppercase; line-height: 1.4; }
  .contact { font-size: 15px; line-height: 1.5; margin-top: 6px; }
  .contact .label { color: var(--accent-blue); font-weight: 700; }
</style>
</head>
<body>
  <section class="card card--front" aria-label="Business card front">
    <p class="brand"><span class="brand-mark" aria-hidden="true"></span>Peak Ridge Base</p>
  </section>

  <section class="card card--back" aria-label="Business card back">
    <div class="back-top">
      <p class="brand"><span class="brand-mark" aria-hidden="true"></span>Peak Ridge Base</p>
      <ul class="services">
        <li class="line-start">Assessment</li><li>Massage</li><li>Physiotherapy</li>
        <li class="break"></li>
        <li class="line-start">Pilates</li><li>Suspension Training</li>
        <li class="break"></li>
        <li class="line-start">Kinesiotaping</li><li>In Any Combination.</li>
      </ul>
    </div>
    <div class="back-bottom">
      <h1 class="tagline">Peak-Ridge-Base for Movers</h1>
      <div class="details">
        <p class="address">17 Halden Rise, Larchmont,<br>Wescombe</p>
        <p class="contact">
          <span class="label">P:</span> 027 418 7093<br>
          <span class="label">E:</span> kerry.dunlow@vestmail.test
        </p>
      </div>
    </div>
  </section>
</body>
</html>
```